Black Granite Web Design Project

We are looking for a design for a new company that will be selling Black Granite slabs and tiles. We will be selling to both end-consumers and granite installers. We have already settled on a logo and hopefully this will give an idea of what we like in our designs. We are not going to be selling online but want people to call us so the site is basically an enhanced business card. We will be focusing a lot on SEO so the design will have to keep that in mind.

We would like to keep the design in 1024x768 to make it easily view-able on all devices.

Regarding navigation there should only be a few sub-pages, like "Granite Slabs", "Granite Tiles", "Delivery", "Contact"

Aside from that we are open to designs. One idea we did have was to personalize the site and have a person there somehow to represent the company, making the user feel there are real people behind this site. This is just an idea and not a must.

The name of the company and site is "Silver Brook Petrano"

Thanks
Updates

Hello All,

Thanks for the great designs. There are some good looking designs that show beautiful kitchens but this site is made for the granite installers and not the retail consumers. So in order not to to confuse the buyers I would like to keep this as much about the raw products as possible. The raw products being the granite slabs, thereby making it obvious we don't sell granite counter tops. 

This design will really be the identity of this company so it is important we get the right message across on this index page and that this page is as complete as possible.

Again, thanks for all the work being put into this.

Target Market(s)

The target audience is granite installers or companies that would with granite slabs.

Industry/Entity Type

Business

```html
<!DOCTYPE html>
<html lang="en">
<head>
<meta charset="utf-8">
<title>Silver Brook Petrano — Granite Slabs &amp; Tiles</title>
<link href="https://fonts.googleapis.com/css2?family=Archivo+Narrow:wght@400;500;600;700&display=swap" rel="stylesheet">
<style>
  :root {
    --page-bg: #efeee8;
    --tile-1: #e8e7e1;
    --tile-2: #dfded8;
    --tile-3: #e3e2dc;
    --tile-4: #eae9e3;
    --ink: #1c1c1c;
    --heading: #2b2b2b;
    --nav: #555555;
    --nav-active: #111111;
    --footer-bg: #0d0d0d;
    --footer-link: #6b6b6b;
    --footer-mark: #ffffff;
  }
  * { box-sizing: border-box; margin: 0; padding: 0; }
  html, body {
    width: 1200px;
    height: 900px;
    overflow: hidden;
  }
  body {
    position: relative;
    background: var(--page-bg);
    font-family: Arial, Helvetica, sans-serif;
    color: var(--ink);
  }
  .site-header {
    position: absolute;
    left: 0; top: 0;
    width: 1200px;
    height: 130px;
  }
  .brand {
    position: absolute;
    left: 36px;
    top: 48px;
    display: flex;
    align-items: center;
    gap: 16px;
  }
  .brand-square {
    width: 52px;
    height: 52px;
    background: var(--ink);
  }
  .brand-name {
    font-family: "Archivo Narrow", "Arial Narrow", sans-serif;
    font-weight: 700;
    font-size: 38px;
    letter-spacing: 0.5px;
    text-transform: uppercase;
    color: var(--ink);
    line-height: 1;
  }
  .main-nav {
    position: absolute;
    right: 64px;
    top: 55px;
    display: flex;
    gap: 29px;
  }
  .main-nav a {
    font-family: "Archivo Narrow", "Arial Narrow", sans-serif;
    font-size: 15px;
    text-transform: uppercase;
    color: var(--nav);
    text-decoration: none;
  }
  .main-nav a.is-active { color: var(--nav-active); }

  .tile {
    position: absolute;
  }
  .tile-a { left: 68px;  top: 193px; width: 203px; height: 202px; background: var(--tile-1); }
  .tile-b { left: 272px; top: 326px; width: 152px; height: 152px; background: var(--tile-2); }
  .tile-c { left: 427px; top: 421px; width: 86px;  height: 84px;  background: var(--tile-3); }
  .tile-d { left: 195px; top: 478px; width: 76px;  height: 76px;  background: var(--tile-4); }
  .tile-e { left: 511px; top: 218px; width: 204px; height: 202px; background: var(--tile-4); }
  .tile-f { left: 715px; top: 166px; width: 52px;  height: 52px;  background: var(--tile-3); }
  .tile-g { left: 714px; top: 421px; width: 117px; height: 152px; background: var(--tile-3); }

  .company-person {
    position: absolute;
    left: 808px;
    top: 130px;
    width: 300px;
    height: 607px;
    border-radius: 70px 70px 0 0;
    background: linear-gradient(180deg, #c9a58d 0%, #cfc9c2 18%, #d6d3ce 55%, #c7c4bf 78%, #5a7fb2 88%, #3f659b 100%);
  }

  .intro {
    position: absolute;
    left: 82px;
    top: 553px;
    width: 680px;
  }
  .intro-title {
    font-family: "Archivo Narrow", "Arial Narrow", sans-serif;
    font-weight: 600;
    font-size: 28px;
    color: var(--heading);
    letter-spacing: 0.3px;
    text-transform: uppercase;
    line-height: 1.2;
  }
  .intro-text {
    margin-top: 21px;
    font-size: 14.5px;
    line-height: 22px;
    color: var(--ink);
  }

  .site-footer {
    position: absolute;
    left: 0; top: 737px;
    width: 1200px;
    height: 163px;
    background: var(--footer-bg);
  }
  .footer-nav {
    position: absolute;
    top: 33px;
    left: 0; width: 100%;
    display: flex;
    justify-content: center;
    gap: 26px;
  }
  .footer-nav a {
    font-family: "Archivo Narrow", "Arial Narrow", sans-serif;
    font-size: 12.5px;
    color: var(--footer-link);
    text-decoration: none;
  }
  .footer-brand {
    position: absolute;
    top: 88px;
    left: 0; width: 100%;
    display: flex;
    justify-content: center;
    align-items: center;
    gap: 6px;
  }
  .footer-brand-square {
    width: 14px;
    height: 14px;
    background: var(--footer-mark);
  }
  .footer-brand-name {
    font-family: "Archivo Narrow", "Arial Narrow", sans-serif;
    font-weight: 700;
    font-size: 13px;
    text-transform: uppercase;
    color: var(--footer-mark);
  }
</style>
</head>
<body>
  <header class="site-header">
    <div class="brand">
      <span class="brand-square"></span>
      <span class="brand-name">Silver Brook Petrano</span>
    </div>
    <nav class="main-nav">
      <a href="#" class="is-active">Home</a>
      <a href="#">Granite Slabs</a>
      <a href="#">Granite Tiles</a>
      <a href="#">Delivery</a>
      <a href="#">Contact</a>
    </nav>
  </header>

  <div class="tile tile-a"></div>
  <div class="tile tile-b"></div>
  <div class="tile tile-c"></div>
  <div class="tile tile-d"></div>
  <div class="tile tile-e"></div>
  <div class="tile tile-f"></div>
  <div class="tile tile-g"></div>

  <div class="company-person" role="img" aria-label="Photo of a smiling company representative in a light linen shirt and blue jeans"></div>

  <section class="intro">
    <h1 class="intro-title">Quisque volutpat mattis eros</h1>
    <p class="intro-text">Lorem ipsum dolor sit amet, consectetuer adipiscing elit. Donec odio. Quisque volutpat mattis eros.<br>Nullam malesuada erat ut turpis. Suspendisse urna nibh, viverra non, semper suscipit, posuere a, pede.</p>
  </section>

  <footer class="site-footer">
    <nav class="footer-nav">
      <a href="#">Home</a>
      <a href="#">Granite Slabs</a>
      <a href="#">Granite Tiles</a>
      <a href="#">Delivery</a>
      <a href="#">Contact</a>
    </nav>
    <div class="footer-brand">
      <span class="footer-brand-square"></span>
      <span class="footer-brand-name">Silver Brook Petrano</span>
    </div>
  </footer>
</body>
</html>
```